Flyer Design Project for gym that sells on results and service

We've operated for 23 yrs and have always sold on friendly service and ensuring our customers get good results in an uncrowded relaxed atmosphere. However a lot of cheap (no service) gyms have opened recently in our area. They sell mostly on price and sometimes on 24 hr trading.

I would like a letterbox flyer with the concept "Are you wasting good money on a gym membership that's not getting you results?".

We would offer the member from the other club a $50 rebate off our fees to cover their cancellation fee at that club and a free PERSONAL TRAINING SESSION and A BONUS FREE MONTH to come over to us.

Ideas would include a graphic of a frustrated or unhappy person (male and female if possible + 25 -35yo) who is standing on scales, looking in the mirror or trying to zip up a dress. It could also include a graphic of a $50 note being passed on.

All my previous designs have been quirky to catch the attention of the homeowner and I don't want to sacrifice the clarity of the message with a flashy busy design.
Updates

I am interested to use simple, clean, hand drawn characters on flyer. The flyer will be 2 sided DL size. Full colour is fine. I like the idea of having a non-busy design. I think I'd prefer not to use typical gym photos as it may limit the appeal of the flyer. I also would like to feature the headline "Are you wasting money on a gym membership that's not getting you results?"

Reason: I am away for 4 days from tomorrow so I've extended the deadline to give more time. Thanks

I've decided to change the headline to "Don't waste your money on a gym membership that doesn't get you results" 

Reason: Sorry guys. I was away and just got back.

Hi 

This is the text I'm planning for the reverse side of the flyer. Sorry about the size of it but I just lifted it from the website. 

Thanks Gavin    

Have you ever started an exercise program to get yourself 'fit and healthy' only to lose motivation and give up 5 or 6 weeks later? Well join the club. Studies tell us that thousands of people do exactly that every year.

Why do so many do this?

Well it turns out there are two distinct groups of people when it comes to exercise. The first group are those who are naturally driven and motivated and the second group (which we estimate to be more than 85% of us) just don't have enough motivation or knowledge to do it on our own.

Which brings us to the problem.

Most gyms sell memberships that really only suit the highly motivated person. They don't have any 'genuine' plan to keep the other 85% motivated to get the results they really want.

Instead they tend to offer 'cheap deals' '24hr access' and 'flashy equipment' in an attempt to convince you that these things will help you get results. These gyms often don't even employ qualified staff to help you reach your goals! Instead they use contractors who prowl around trying to sell you their personal training services.

OK! That's the other guys ... Then there's us.

Ater 23 years here at Corvel I can tell you and the only reason we're still here today is the effort we put in to help our members get the results they want.

Sure you can by a cheap membership here (if that's what you really need) but what we're famous for is our 'Service Packages' which give our members access to high quality trainers at very reasonable prices. These packages are designed to help you stay focussed and motivated and to give you the knowledge and tools to actually acheive what you wanted in the first place.. GREAT RESULTS!

So what are you waiting for? Get the body and vitality you've always wanted today.

Just call us today on 55 318462 to talk to a qualified trainer about your goals or CLICK HERE for a FREE 3 day pass.

i'd also like the reverse side to show that we will offering (for the next 7days only) A $2 Joining Fee, No Payments for 1st 30 days + a FREE Personal Training Session.   

Industry/Entity Type

Club

Requirements
Nice to have
• I quite like the idea of the hand drawn characters on the artflockery intro video.

```html
<!DOCTYPE html>
<html lang="en">
<head>
<meta charset="utf-8">
<title>Corvel Fitness – DL Flyer</title>
<link rel="stylesheet" href="https://fonts.googleapis.com/css2?family=Montserrat:wght@600;700;800&family=Open+Sans:wdth,wght@75..100,300..800&display=swap">
<style>
  :root {
    --page: #e6e7e9;
    --navy: #134576;
    --blue: #1d5d9c;
    --blue-light: #2a70b3;
    --red: #e12b2b;
    --red-dark: #b5191c;
    --white: #ffffff;
    --cream: #f7efd6;
    --pink: #e0456b;
  }
  * { box-sizing: border-box; margin: 0; padding: 0; }
  html, body { width: 1169px; height: 1200px; overflow: hidden; }
  body {
    background: var(--page);
    font-family: "Open Sans", Arial, sans-serif;
    position: relative;
  }
  .flyer-side {
    position: absolute;
    top: 86px;
    width: 473px;
    height: 993px;
    color: var(--white);
    overflow: hidden;
  }
  .front {
    left: 73px;
    background: linear-gradient(158deg, var(--blue) 0 33%, var(--navy) 33% 62%, var(--blue) 62% 100%);
  }
  .back {
    left: 596px;
    background: linear-gradient(152deg, var(--blue) 0 28%, var(--navy) 28% 52%, var(--blue) 52% 74%, var(--navy) 74%);
  }

  /* Front */
  .headline {
    position: absolute;
    top: 16px; left: 0; right: 0;
    font-family: "Montserrat", Arial, sans-serif;
    font-weight: 700;
    font-size: 35px;
    line-height: 49px;
    text-align: center;
  }
  .headline .accent { color: var(--red); }
  .illustration {
    position: absolute;
    top: 254px; left: 60px;
    width: 369px; height: 536px;
    background: linear-gradient(180deg, var(--cream) 0%, #efe4c4 100%);
    clip-path: polygon(0 16%, 100% 0, 100% 100%, 0 100%);
  }
  .illustration .figure-tone {
    position: absolute; left: 40px; bottom: 40px;
    width: 140px; height: 320px;
    background: linear-gradient(180deg, #f3d77a 0%, var(--pink) 55%, #c93357 100%);
    border-radius: 60px 60px 10px 10px;
    opacity: 0.55;
  }
  .illustration .mirror-tone {
    position: absolute; right: 30px; top: 60px;
    width: 140px; height: 430px;
    background: linear-gradient(180deg, #f6f6f6 0%, #f4c7d3 60%, #e9e9e9 100%);
    border-radius: 70px 70px 6px 6px;
    opacity: 0.8;
  }
  .deal-badge {
    position: absolute;
    top: 655px; left: 303px;
    width: 156px; height: 150px;
  }
  .offer-lines {
    position: absolute;
    top: 814px; left: 0; right: 0;
    text-align: center;
    font-weight: 700;
    font-size: 19px;
    line-height: 31px;
  }
  .front-footer {
    position: absolute;
    left: 0; right: 0; top: 898px;
    height: 76px;
    background: var(--blue-light);
    display: flex;
    align-items: center;
  }
  .brand {
    width: 186px; height: 76px;
    margin-left: 14px;
    flex-shrink: 0;
    background: var(--white);
    display: flex; align-items: center; justify-content: center; gap: 8px;
    color: var(--red-dark);
    font-weight: 700;
    font-size: 18px;
  }
  .brand .dot { width: 13px; height: 13px; border-radius: 50%; background: var(--red-dark); }
  .address { margin-left: 15px; font-size: 18px; white-space: nowrap; }

  /* Back */
  .copy {
    position: absolute;
    left: 26px; right: 22px;
    font-size: 14.4px;
    font-stretch: 90%;
    line-height: 20px;
    text-align: justify;
  }
  .copy p + p { margin-top: 8px; }
  .copy h2 {
    font-size: 16.5px;
    font-weight: 700;
    font-stretch: 100%;
    margin: 16px 0 7px;
  }
  .copy-top { top: 28px; }
  .copy-bottom { top: 544px; }
  .strong-cta { font-weight: 700; font-size: 19px; letter-spacing: 0.5px; }
  .red-bar {
    position: absolute;
    top: 488px; left: 0; right: 0;
    height: 38px;
    background: var(--red);
    font-weight: 700;
    font-size: 17px;
    line-height: 38px;
    text-align: center;
  }
  .offer-tag {
    position: absolute;
    top: 873px; left: 10px;
    height: 32px; padding: 0 18px;
    background: var(--red);
    font-weight: 700; font-size: 16.5px; line-height: 32px;
  }
  .offer-detail {
    position: absolute;
    top: 915px; left: 26px; right: 10px;
    font-weight: 700;
    font-size: 14.5px;
    font-stretch: 82%;
    line-height: 30px;
    white-space: nowrap;
  }
</style>
</head>
<body>

<section class="flyer-side front">
  <h1 class="headline">“ DON’T <span class="accent">WASTE</span> YOUR<br>MONEY ON A GYM<br>MEMBERSHIP<br>THAT DOESN’T GET<br>YOU RESULTS ”</h1>

  <div class="illustration" role="img" aria-label="Hand-drawn woman in a tight pink dress looking puzzled at her reflection in a mirror">
    <div class="mirror-tone"></div>
    <div class="figure-tone"></div>
  </div>

  <svg class="deal-badge" viewBox="0 0 150 150" aria-label="Hot deal, first 25 new members only">
    <polygon fill="#ffffff" points="75,2 87,20 107,8 110,31 134,28 126,50 148,60 130,75 148,90 126,100 134,122 110,119 107,142 87,130 75,148 63,130 43,142 40,119 16,122 24,100 2,90 20,75 2,60 24,50 16,28 40,31 43,8 63,20"/>
    <polygon fill="#c41d23" points="75,10 86,26 104,16 106,36 127,34 120,53 140,62 124,75 140,88 120,97 127,116 106,114 104,134 86,124 75,140 64,124 46,134 44,114 23,116 30,97 10,88 26,75 10,62 30,53 23,34 44,36 46,16 64,26"/>
    <g fill="#ffffff" font-family="Open Sans, Arial, sans-serif" font-weight="700" text-anchor="middle" style="font-stretch:80%">
      <text x="75" y="59" font-size="17" textLength="82" lengthAdjust="spacingAndGlyphs">HOT DEAL</text>
      <text x="75" y="78" font-size="13" textLength="68" lengthAdjust="spacingAndGlyphs">1st 25 NEW</text>
      <text x="75" y="97" font-size="16" textLength="76" lengthAdjust="spacingAndGlyphs">MEMBERS</text>
      <text x="75" y="114" font-size="13" textLength="34" lengthAdjust="spacingAndGlyphs">ONLY</text>
    </g>
  </svg>

  <div class="offer-lines">
    <p>$2 TO JOIN - No payments for 30 days</p>
    <p>FREE PERSONAL TRAINING SESSION</p>
  </div>

  <footer class="front-footer">
    <div class="brand"><span class="dot"></span>Corvel Fitness</div>
    <p class="address">Add: 18 Lantern Ave Corvel</p>
  </footer>
</section>

<section class="flyer-side back">
  <div class="copy copy-top">
    <p>Have you ever started an exercise program to get yourself 'fit and healthy' only to lose motivation and give up 5 or 6 weeks later? Well join the club. Studies tell us that thousands of people do exactly that every year.</p>
    <h2>WHY DO SO MANY DO THIS?</h2>
    <p>Well it turns out there are two distinct groups of people when it comes to exercise. The first group are those who are naturally driven and motivated and the second group (which we estimate to be more than 85% of us) just don't have enough motivation or knowledge to do it on our own.</p>
    <h2>WHICH BRINGS US TO THE PROBLEM ?</h2>
    <p>Most gyms sell memberships that really only suit the highly motivated person. They don't have any 'genuine' plan to keep the other 85% motivated to get the results they really want.</p>
    <p>Instead they tend to offer 'cheap deals' '24hr access' and 'flashy equipment' in an attempt to convince you that these things will help you get results. These gyms often don't even</p>
  </div>

  <div class="red-bar">OK! THAT'S THE OTHER GUYS...THEN THERE'S US.</div>

  <div class="copy copy-bottom">
    <p>After 23 years here at Corvel I can tell you and the only reason we're still here today is the effort we put in to help our members get the results they want.</p>
    <p>Sure you can by a cheap membership here (if that's what you really need) but what we're famous for is our 'Service Packages' which give our members access to high quality trainers at very reasonable prices. These packages are designed to help you stay focussed and motivated and to give you the knowledge and tools to actually acheive what you wanted in the first place.. <strong>GREAT RESULTS</strong> !</p>
    <p>So what are you waiting for? Get the body and vitality you've always wanted today.</p>
    <p>Just call us today on <span class="strong-cta">55 318462</span> to talk to a qualified trainer about your goals.</p>
  </div>

  <div class="offer-tag">WE WILL OFFERING :</div>
  <div class="offer-detail">
    <p>( For the next 7days only )&nbsp; A $2 JOINING FEE</p>
    <p>No Payments for 1st 30 days + A&nbsp; FREE PERSONAL TRAINING SESSION.</p>
  </div>
</section>

</body>
</html>
```